Design logo and business card.

Design and construct logo and card for my business which is an over seeing company of other smaller businesses. The companies name is quarry5 business collective. Im open to any ideas but i am looking for a very cool contemporary design with a very prestige feel. The card can be either single or double sided, Thank you and i will look forward to your submissions.

Industry/Entity Type

Business

Requirements
Must have
• Company name, email, website, telephone, my name. Cool modern look with a prestige feel.

```html
<!DOCTYPE html>
<html lang="en">
<head>
<meta charset="utf-8">
<title>quarry5 business collective – business card</title>
<link rel="stylesheet" href="https://fonts.googleapis.com/css2?family=Cormorant+Garamond:wght@500&display=swap">
<style>
  :root {
    --paper: #ffffff;
    --swirl-grey: #3a3a3a;
    --band-black: #000000;
    --text-dark: #111111;
  }
  * { margin: 0; padding: 0; box-sizing: border-box; }
  html, body {
    width: 1200px;
    height: 686px;
    overflow: hidden;
    background: var(--paper);
  }
  .card {
    position: relative;
    width: 1200px;
    height: 686px;
    background: var(--paper);
    font-family: "Cormorant Garamond", Georgia, serif;
    font-weight: 500;
  }
  .brand-band {
    position: absolute;
    left: 0;
    top: 0;
    width: 1200px;
    height: 494px;
    background: var(--band-black);
    overflow: hidden;
  }
  .ornament-area {
    position: absolute;
    left: 0;
    top: 0;
    width: 720px;
    height: 494px;
    background: radial-gradient(ellipse at 35% 45%, var(--swirl-grey) 0%, #1c1c1c 40%, var(--band-black) 75%);
    opacity: 0.8;
  }
  .wordmark-name,
  .wordmark-tagline {
    position: absolute;
    color: var(--paper);
    line-height: 1;
    white-space: nowrap;
  }
  .wordmark-name {
    right: 57px;
    top: 126px;
    font-size: 160px;
  }
  .wordmark-tagline {
    left: 520px;
    top: 299px;
    font-size: 61px;
  }
  .contact-row {
    position: absolute;
    left: 0;
    top: 494px;
    width: 1200px;
    height: 192px;
    color: var(--text-dark);
  }
  .contact-row p {
    position: absolute;
    line-height: 1;
    white-space: nowrap;
  }
  .person-name {
    left: 71px;
    top: 60px;
    font-size: 64px;
  }
  .phone {
    left: 423px;
    top: 54px;
    font-size: 50px;
  }
  .website,
  .email {
    left: 766px;
    width: 400px;
    text-align: center;
    font-size: 52px;
  }
  .website { top: 23px; }
  .email { top: 97px; }
</style>
</head>
<body>
  <div class="card">
    <header class="brand-band">
      <div class="ornament-area" role="img" aria-label="Faint grey flourish of curling swirls"></div>
      <span class="wordmark-name">quarry5</span>
      <span class="wordmark-tagline">business collective</span>
    </header>
    <section class="contact-row">
      <p class="person-name">Leo Marsh</p>
      <p class="phone">+34 611 204 587</p>
      <p class="website">quarry-5.com</p>
      <p class="email">info@quarry-5.com</p>
    </section>
  </div>
</body>
</html>
```